Tidewell Recovery Business Card Design

Professional and clean design. The design colors should flow with the logo. Two-sided card with the website on the back which is:

www.TidewellRecovery.example.

"Specializing in Water Damage Restoration"

On the front I need the name, email, phone, and logo.

Name: Dorian Vashti
Email: Dorian@TidewellRecovery.example
Phone: 555-318-2046 for now

I only have the Preview and Thumbnail right now but should have the source files uploaded within a day or two.

Target Market(s)

Flood victims, home owners with water damage from busted pipes etc...

Industry/Entity Type

Business

Contact Information for Business Card

Name: Dorian Vashti

Font styles to use
Serif
Sans Serif

```html
<!DOCTYPE html>
<html lang="en">
<head>
<meta charset="utf-8">
<title>Tidewell Recovery – Business Card</title>
<link rel="stylesheet" href="https://fonts.googleapis.com/css2?family=Cinzel:wght@600&family=Open+Sans:wght@400;700&display=swap">
<style>
  :root {
    --stage: #eef1f3;
    --card-white: #ffffff;
    --brand-blue: #2ea9da;
    --brand-blue-deep: #1b8fc4;
    --brand-blue-light: #5cc3e8;
    --ink-blue: #35abdc;
  }
  * { margin: 0; padding: 0; box-sizing: border-box; }
  html, body {
    width: 1200px;
    height: 780px;
    overflow: hidden;
    background: var(--stage);
  }
  .stage {
    width: 1200px;
    height: 780px;
    display: flex;
    align-items: center;
    justify-content: center;
  }
  .business-card {
    position: relative;
    width: 840px;
    height: 480px;
    background: var(--card-white);
    box-shadow: 0 10px 30px rgba(0, 40, 70, 0.18);
    overflow: hidden;
  }
  .card-shapes {
    position: absolute;
    inset: 0;
    width: 100%;
    height: 100%;
  }
  .brand-block {
    position: absolute;
    top: 70px;
    left: 250px;
    width: 430px;
    text-align: center;
  }
  .brand-mark-row {
    display: flex;
    align-items: center;
    justify-content: center;
    gap: 18px;
  }
  .brand-dot {
    width: 58px;
    height: 58px;
    border-radius: 50%;
    background: var(--brand-blue);
    flex: none;
  }
  .brand-name {
    font-family: "Cinzel", Georgia, serif;
    font-weight: 600;
    font-size: 38px;
    color: var(--brand-blue);
    letter-spacing: 1px;
    white-space: nowrap;
  }
  .brand-tagline {
    margin-top: 14px;
    font-family: "Open Sans", Arial, sans-serif;
    font-size: 17px;
    color: var(--ink-blue);
  }
  .contact-block {
    position: absolute;
    left: 170px;
    top: 268px;
    font-family: "Open Sans", Arial, sans-serif;
    color: var(--ink-blue);
  }
  .holder-name {
    font-weight: 700;
    font-size: 30px;
    margin-bottom: 10px;
  }
  .contact-list { list-style: none; }
  .contact-item {
    display: flex;
    align-items: center;
    gap: 12px;
    font-size: 21px;
    line-height: 33px;
  }
  .contact-icon {
    width: 24px;
    height: 24px;
    flex: none;
  }
</style>
</head>
<body>
<main class="stage">
  <section class="business-card" aria-label="Tidewell Recovery business card, front">
    <svg class="card-shapes" viewBox="0 0 840 480" aria-hidden="true">
      <defs>
        <linearGradient id="sideBlue" x1="0" y1="0" x2="1" y2="1">
          <stop offset="0" stop-color="var(--brand-blue-light)"/>
          <stop offset="1" stop-color="var(--brand-blue-deep)"/>
        </linearGradient>
      </defs>
      <rect width="840" height="480" fill="url(#sideBlue)"/>
      <path d="M120 0 L690 0 Q860 250 760 480 L150 480 Q20 300 120 0 Z" fill="var(--card-white)"/>
    </svg>

    <div class="brand-block">
      <div class="brand-mark-row">
        <span class="brand-dot"></span>
        <span class="brand-name">Tidewell Recovery</span>
      </div>
      <p class="brand-tagline">Specializing in Water Damage Restoration</p>
    </div>

    <div class="contact-block">
      <p class="holder-name">Dorian Vashti</p>
      <ul class="contact-list">
        <li class="contact-item">
          <svg class="contact-icon" viewBox="0 0 24 24" aria-hidden="true">
            <rect width="24" height="24" rx="3" fill="var(--brand-blue)"/>
            <path d="M7 5 L10 5 L11 9 L9 10.5 Q10.5 13.5 13.5 15 L15 13 L19 14 L19 17 Q18 19 15 18.5 Q7 16 5.5 8 Q5 6 7 5 Z" fill="#fff"/>
          </svg>
          555-318-2046
        </li>
        <li class="contact-item">
          <svg class="contact-icon" viewBox="0 0 24 24" aria-hidden="true">
            <rect width="24" height="24" rx="3" fill="var(--brand-blue)"/>
            <rect x="5" y="7" width="14" height="10" fill="none" stroke="#fff" stroke-width="1.6"/>
            <path d="M5 7 L12 13 L19 7" fill="none" stroke="#fff" stroke-width="1.6"/>
          </svg>
          Dorian@TidewellRecovery.example
        </li>
        <li class="contact-item">
          <svg class="contact-icon" viewBox="0 0 24 24" aria-hidden="true">
            <rect width="24" height="24" rx="3" fill="var(--brand-blue)"/>
            <circle cx="12" cy="12" r="7" fill="none" stroke="#fff" stroke-width="1.5"/>
            <ellipse cx="12" cy="12" rx="3" ry="7" fill="none" stroke="#fff" stroke-width="1.2"/>
            <path d="M5 12 H19 M6.5 8.5 H17.5 M6.5 15.5 H17.5" stroke="#fff" stroke-width="1.2"/>
          </svg>
          www.TidewellRecovery.example
        </li>
      </ul>
    </div>
  </section>
</main>
</body>
</html>
```